Website customization using WordPress Theme already purchased

Need informational website for Orla Brightwell LLC. Orla Brightwell is investment group company for multiple cloud based products and website. We need website for anyone coming to our website to be able get information on our products. I already have WordPress theme that I would like to use. Right person/company will be able to customize WordPress theme to our needs and be able to give us final product of 7-9 pages of complete website.

Industry/Entity Type

Investment

Number of Pages Required

5+ page

Colors
add136
3176b5
ec1f27
f37122

```html
<!DOCTYPE html>
<html lang="en">
<head>
<meta charset="utf-8">
<title>Orla Brightwell LLC</title>
<link rel="stylesheet" href="https://fonts.googleapis.com/css2?family=Montserrat:wght@400;500;600;700&family=Open+Sans:ital,wght@0,400;0,600;1,400&display=swap">
<style>
:root{
  --green:#add136;
  --blue:#3176b5;
  --footer-blue:#2f6db0;
  --orange:#f37122;
  --red:#ec1f27;
  --ink:#222;
  --body:#666;
  --grey-band:#f0f0f0;
  --line:#dcdcdc;
  --night-a:#0e2a45;
  --night-b:#1c4c5c;
}
*{margin:0;padding:0;box-sizing:border-box}
html,body{width:698px;height:1200px;overflow:hidden;background:#fff}
body{position:relative;font-family:"Open Sans",Arial,sans-serif;color:var(--body)}
.abs{position:absolute}
.head{font-family:"Montserrat",Arial,sans-serif;color:var(--ink);font-weight:600;text-transform:uppercase}

/* hero */
.hero{position:absolute;left:0;top:0;width:698px;height:322px;
  background:radial-gradient(ellipse at 70% 40%,#21506a 0%,var(--night-b) 30%,var(--night-a) 75%,#0a1e33 100%)}
.topbar{position:absolute;left:0;top:0;width:698px;height:3px;
  background:linear-gradient(90deg,var(--red),var(--orange),var(--green),var(--blue))}
.navline{position:absolute;left:0;top:51px;width:698px;height:1px;background:rgba(255,255,255,.2)}
.brand{position:absolute;display:flex;align-items:center;color:#fff;font-family:"Montserrat",Arial,sans-serif;font-weight:700;white-space:nowrap}
.brand .dot{border-radius:50%;background:#fff}
.nav{position:absolute;left:0;top:21px;width:698px;height:12px;font-family:"Montserrat",Arial,sans-serif;font-weight:500;font-size:8.5px;color:#fff}
.nav span{position:absolute;top:0;white-space:nowrap}
.nav .on{color:var(--green)}
.social{position:absolute;display:flex}
.social span{display:block;border-radius:50%;border:1px solid rgba(255,255,255,.8)}
.hero h1{position:absolute;left:58px;top:112px;font-family:"Montserrat",Arial,sans-serif;font-weight:700;font-size:22px;color:#fff;letter-spacing:.2px;white-space:nowrap}
.hero .rule{position:absolute;left:58px;top:153px;width:307px;height:1px;background:rgba(255,255,255,.6)}
.hero p{position:absolute;left:58px;top:165px;width:310px;font-size:10.3px;line-height:18.5px;color:#fff}
.btn{position:absolute;top:215px;height:24px;font-family:"Montserrat",Arial,sans-serif;font-weight:700;font-size:8px;color:#fff;display:flex;align-items:center;justify-content:center;letter-spacing:.3px}
.btn.fill{left:58px;width:87px;background:var(--green)}
.btn.line{left:153px;width:86px;border:1px solid #fff}
.devices{position:absolute;left:397px;top:90px;width:264px;height:206px;
  background:linear-gradient(160deg,#c9ced4 0%,#3a4a5a 45%,#1a2a3a 100%);border-radius:6px;opacity:.9}
.dots{position:absolute;top:286px;left:327px;display:flex;gap:2px}
.dots span{width:10px;height:10px;border-radius:50%;border:1px solid #fff}
.dots span.on{background:#fff}

/* welcome */
.center{left:0;width:698px;text-align:center}
.welcome-title{top:352px;font-size:14.5px;letter-spacing:.2px}
.welcome-text{top:380px;left:120px;width:458px;font-size:7px;line-height:15px;text-align:center}
.step-title{position:absolute;top:527px;width:200px;text-align:center;font-size:10.5px}
.step-text{position:absolute;top:547px;width:180px;text-align:center;font-size:6.8px;line-height:13.5px}

/* grey band */
.band{position:absolute;left:0;top:612px;width:698px;height:248px;background:var(--grey-band)}
.sec-title{font-size:13.5px;top:636px}
.card{position:absolute;left:58px;top:674px;width:265px;height:159px;background:#fff;border:1px solid var(--line)}
.avatar{position:absolute;left:31px;top:685px;width:54px;height:54px;border-radius:50%;border:3px solid #fff;
  background:radial-gradient(circle at 50% 40%,#d9b39a,#8a7a70 70%);box-shadow:0 0 0 1px var(--line)}
.name{position:absolute;left:101px;top:689px;font-family:"Montserrat",Arial,sans-serif;font-size:12px;color:var(--ink)}
.role{position:absolute;left:101px;top:707px;font-size:8.5px;font-style:italic;color:var(--blue)}
.quote{position:absolute;left:101px;top:730px;width:210px;font-size:6.5px;line-height:14.5px}
.tdots{position:absolute;left:102px;top:798px;display:flex;gap:3px}
.tdots span{width:7px;height:7px;border-radius:50%;background:#d6d6d6}
.tdots span.on{background:var(--green)}
.news-img{position:absolute;left:374px;width:72px;height:60px}
.news-title{position:absolute;left:459px;width:190px;font-family:"Montserrat",Arial,sans-serif;font-weight:600;font-size:9.3px;line-height:15px;color:#333}
.news-meta{position:absolute;left:459px;font-size:6.8px;color:var(--blue)}
.divider{position:absolute;left:374px;width:267px;height:1px;background:var(--line)}
.more{position:absolute;left:520px;top:828px;width:121px;text-align:right;font-family:"Montserrat",Arial,sans-serif;font-weight:600;font-size:6.8px;color:var(--green)}

/* companies */
.companies-title{top:885px;font-size:14.5px}
.company{position:absolute;top:925px;width:134px;height:58px;border:1px solid var(--line);box-shadow:0 1px 2px rgba(0,0,0,.08);
  display:flex;align-items:center;justify-content:center;font-family:"Montserrat",Arial,sans-serif;font-weight:700;font-size:15px;color:#bdbdbd}

/* footer */
.footer{position:absolute;left:0;top:1010px;width:698px;height:154px;background:var(--footer-blue);color:#fff}
.foot-h{position:absolute;top:1034px;font-family:"Montserrat",Arial,sans-serif;font-weight:600;font-size:9.5px;color:#fff}
.links{position:absolute;left:227px;top:1057px;font-size:7px;line-height:14px;color:#fff;list-style:none}
.foot-text{position:absolute;font-size:6.8px;line-height:10px;color:#fff}
.email{position:absolute;left:338px;top:1085px;width:148px;height:21px;background:#fff;font-size:6.5px;color:#aaa;padding:6px 8px}
.subscribe{position:absolute;left:338px;top:1116px;width:54px;height:18px;background:var(--green);font-family:"Montserrat",Arial,sans-serif;font-weight:600;font-size:6.3px;color:#fff;display:flex;align-items:center;justify-content:center}
.contact-row{position:absolute;left:523px;display:flex;gap:8px;font-size:6.8px;line-height:10px;color:#fff}
.contact-row svg{flex:none;margin-top:1px}
.copyright{position:absolute;left:58px;top:1177px;font-size:6.8px;color:#666}
.social.foot span{border:1px solid #bbb}
</style>
</head>
<body>

<header class="hero">
  <div class="topbar"></div>
  <div class="brand" style="left:58px;top:11px;font-size:10.5px;gap:6px">
    <span class="dot" style="width:32px;height:32px"></span>Orla Brightwell
  </div>
  <nav class="nav">
    <span class="on" style="left:204px">Home</span>
    <span style="left:244px">About Us</span>
    <span style="left:298px">Entrepreneurs</span>
    <span style="left:373px">News</span>
    <span style="left:411px">Companies</span>
    <span style="left:473px">Contact Us</span>
  </nav>
  <svg class="abs" style="left:535px;top:21px" width="10" height="10" viewBox="0 0 10 10" aria-label="Search"><circle cx="4" cy="4" r="3" fill="none" stroke="#fff" stroke-width="1.4"/><line x1="6.2" y1="6.2" x2="9" y2="9" stroke="#fff" stroke-width="1.5"/></svg>
  <div class="social" style="left:558px;top:17px;gap:5px" aria-label="Social links">
    <span style="width:17px;height:17px"></span><span style="width:17px;height:17px"></span><span style="width:17px;height:17px"></span><span style="width:17px;height:17px"></span>
  </div>
  <div class="navline"></div>

  <h1>ORLA BRIGHTWELL LLC</h1>
  <div class="rule"></div>
  <p>At vero eos et accusamus et iusto odio dignissimos ducimu qui blanditiis praesentium voluptatum deleniti.</p>
  <div class="btn fill">GET STARTED</div>
  <div class="btn line">READ MORE</div>
  <div class="devices" role="img" aria-label="Desktop monitor and smartphone showing the company website"></div>
  <div class="dots"><span class="on"></span><span></span><span></span><span></span></div>
</header>

<section>
  <h2 class="head abs center welcome-title">Welcome to Orla Brightwell LLC</h2>
  <p class="abs welcome-text">At vero eos et accusamus et iusto odio dignissimos ducimus qui blanditiis praesentium voluptatum deleniti atque corrupti quos dolores et quas provident, similique sunt in culpa qui officia denihil impedit quo minus id quod maxime placeat facere</p>

  <svg class="abs" style="left:0;top:410px" width="698" height="115" viewBox="0 410 698 115">
    <line x1="186" y1="466" x2="236" y2="466" stroke="var(--blue)"/>
    <line x1="254" y1="466" x2="302" y2="466" stroke="var(--green)"/>
    <line x1="396" y1="466" x2="445" y2="466" stroke="var(--green)"/>
    <line x1="463" y1="466" x2="512" y2="466" stroke="var(--orange)"/>
    <circle cx="245" cy="466" r="8.5" fill="#fff" stroke="var(--blue)"/>
    <path d="M243 462 l4 4 -4 4" fill="none" stroke="var(--blue)"/>
    <circle cx="454" cy="466" r="8.5" fill="#fff" stroke="var(--orange)"/>
    <path d="M452 462 l4 4 -4 4" fill="none" stroke="var(--orange)"/>

    <path d="M138 418 L186 466 L138 514 L90 466 Z" fill="none" stroke="var(--blue)"/>
    <path d="M138 422 L182 466 L138 510 L94 466 Z" fill="var(--blue)"/>
    <rect x="122" y="466" width="6" height="10" fill="#fff"/><rect x="131" y="460" width="6" height="16" fill="#fff"/><rect x="140" y="452" width="6" height="24" fill="#fff"/>
    <path d="M120 462 L138 448 L146 448" fill="none" stroke="#fff" stroke-width="2"/><path d="M146 443 l7 5 -7 5z" fill="#fff"/>
    <line x1="120" y1="478" x2="156" y2="478" stroke="#fff" stroke-width="1.5"/>

    <path d="M349 418 L397 466 L349 514 L301 466 Z" fill="none" stroke="var(--green)"/>
    <path d="M349 422 L393 466 L349 510 L305 466 Z" fill="var(--green)"/>
    <circle cx="349" cy="466" r="16" fill="none" stroke="#fff" stroke-width="2"/>
    <path d="M341 466 l6 6 10 -11" fill="none" stroke="#fff" stroke-width="2.4"/>

    <path d="M559 418 L607 466 L559 514 L511 466 Z" fill="none" stroke="var(--orange)"/>
    <path d="M559 422 L603 466 L559 510 L515 466 Z" fill="var(--orange)"/>
    <rect x="545" y="462" width="14" height="14" fill="none" stroke="#fff" stroke-width="2"/>
    <rect x="552" y="455" width="20" height="20" fill="none" stroke="#fff" stroke-width="2"/>
    <path d="M560 467 l9 -9 M563 458 h6 v6" fill="none" stroke="#fff" stroke-width="2"/>
  </svg>

  <h3 class="head step-title" style="left:38px">Investing</h3>
  <p class="step-text" style="left:48px">Nam libero tempore, cum soluta nobis est eli ndi optio cumque nihil impedit quo minus id quod maxime placeat facere possimu</p>
  <h3 class="head step-title" style="left:249px">Licensing</h3>
  <p class="step-text" style="left:259px">Nam libero tempore, cum soluta nobis est eli ndi optio cumque nihil impedit quo minus id quod maxime placeat facere possimu</p>
  <h3 class="head step-title" style="left:459px">Scaling</h3>
  <p class="step-text" style="left:469px">Nam libero tempore, cum soluta nobis est eli ndi optio cumque nihil impedit quo minus id quod maxime placeat facere possimu</p>
</section>

<section class="band"></section>
<h2 class="head abs sec-title" style="left:58px">Client Testimonials</h2>
<div class="card"></div>
<div class="avatar" role="img" aria-label="Portrait of the client"></div>
<div class="name">Marcus Hale</div>
<div class="role">Finibus Bonorum</div>
<p class="quote">“ At vero eos et accusamus et iusto odio dignissimos ducimuqui blanditiis praesentium voluptatum deleniti atque corrupti quos dolores et quas molestias excepturi sint occaecati cupiditate ro vident, similique sunt in culpa qui officia ”</p>
<div class="tdots"><span class="on"></span><span></span><span></span></div>

<h2 class="head abs sec-title" style="left:373px">Recent News</h2>
<div class="news-img" style="top:674px;background:linear-gradient(180deg,#c9cdd3,#8d949c)" role="img" aria-label="Business people walking in a city plaza"></div>
<div class="news-title" style="top:670px">At vero eos et accusamus et iusto odio dignissimos ducimus qui</div>
<div class="news-meta" style="top:705px">▦ 02/11/2016 &nbsp;| &nbsp;● Marcus Hale</div>
<div class="divider" style="top:740px"></div>
<div class="news-img" style="top:747px;background:linear-gradient(135deg,#1d4f7a,#3f8fc4)" role="img" aria-label="Hand holding a smartphone with charts"></div>
<div class="news-title" style="top:743px">At vero eos et accusamus et iusto odio dignissimos ducimus qui</div>
<div class="news-meta" style="top:779px">▦ 02/11/2016 &nbsp;| &nbsp;● Marcus Hale</div>
<div class="divider" style="top:816px"></div>
<div class="more">VIEW MORE NEWS &gt;&gt;</div>

<section>
  <h2 class="head abs center companies-title">Featured Companies</h2>
  <svg class="abs" style="left:39px;top:946px" width="10" height="16" viewBox="0 0 10 16"><path d="M8 1 L2 8 L8 15" fill="none" stroke="#aaa" stroke-width="1.5"/></svg>
  <div class="company" style="left:58px">Kestrel</div>
  <div class="company" style="left:207px">Tidewell</div>
  <div class="company" style="left:357px">Lumora</div>
  <div class="company" style="left:507px">Brackenfield</div>
  <svg class="abs" style="left:650px;top:946px" width="10" height="16" viewBox="0 0 10 16"><path d="M2 1 L8 8 L2 15" fill="none" stroke="#aaa" stroke-width="1.5"/></svg>
</section>

<footer>
  <div class="footer"></div>
  <div class="brand" style="left:57px;top:1071px;font-size:12px;gap:7px">
    <span class="dot" style="width:40px;height:40px"></span>Orla Brightwell
  </div>
  <h4 class="foot-h" style="left:227px">INFORMATION</h4>
  <ul class="links"><li>Home</li><li>About Us</li><li>Entrepreneurs</li><li>News</li><li>Companies</li><li>Contact Us</li></ul>
  <h4 class="foot-h" style="left:338px">NEWSLETTER SUBSCRIPTION</h4>
  <p class="foot-text" style="left:338px;top:1059px;width:140px">Register your Email Address to get information about us</p>
  <div class="email">Email Address</div>
  <div class="subscribe">SUBSCRIBE</div>
  <h4 class="foot-h" style="left:523px">CONTACT US</h4>
  <div class="contact-row" style="top:1059px">
    <svg width="7" height="9" viewBox="0 0 7 9"><path d="M3.5 9 C1 5.5 0 4.5 0 3.3 A3.5 3.3 0 0 1 7 3.3 C7 4.5 6 5.5 3.5 9Z" fill="#fff"/><circle cx="3.5" cy="3.3" r="1.2" fill="var(--footer-blue)"/></svg>
    <span style="width:110px">418 Harbor Row, Suite 6, Fairmont CA. 95001</span>
  </div>
  <div class="contact-row" style="top:1089px">
    <svg width="8" height="8" viewBox="0 0 8 8"><path d="M1 0 L3 0 L3.5 2 L2.3 3 C3 4.5 3.7 5.2 5 5.8 L6 4.6 L8 5 L8 7 C8 7.6 7.5 8 7 8 C3 7.6 0.4 5 0 1 C0 0.5 0.4 0 1 0Z" fill="#fff"/></svg>
    <span>555 014 2288</span>
  </div>
  <div class="contact-row" style="top:1109px">
    <svg width="9" height="8" viewBox="0 0 9 8"><rect x="0" y="2" width="9" height="6" fill="#fff"/><rect x="2" y="0" width="5" height="3" fill="#fff"/><rect x="2" y="4" width="5" height="1" fill="var(--footer-blue)"/></svg>
    <span>555 014 7730</span>
  </div>
  <div class="contact-row" style="top:1129px">
    <svg width="9" height="7" viewBox="0 0 9 7"><rect width="9" height="7" fill="#fff"/><path d="M0 0 L4.5 4 L9 0" fill="none" stroke="var(--footer-blue)"/></svg>
    <span>info@orlabrightwell.com</span>
  </div>
  <p class="copyright">Copyrights © 2016, Orla Brightwell LLC. All rights reserved.</p>
  <div class="social foot" style="left:550px;top:1172px;gap:4px" aria-label="Social links">
    <span style="width:20px;height:20px"></span><span style="width:20px;height:20px"></span><span style="width:20px;height:20px"></span><span style="width:20px;height:20px"></span>
  </div>
</footer>

</body>
</html>
```